Business Card Design Project for New Home Builder

Double sided card,
Larger logo on 1 side with small quote, Its not just a house, Its your Home, across the bottom. Matt Red base, White logo, black quote??

other side, ,
Its your Home LHS. Smaller logo RHS with.
Details below.

"neuropolitical Rg" Logo Font

Dennis Orford

PO Box 8437 Mildura VIC 3502
Mobile 0427 318865 / Phone 03 50718 962 / Fax 03 50718 415
email DennisO@tbvbuild.net.au
Vic Building Practitioner DB-U 8174 Vic Commercial Builder CB-U 5093
NSW Contractor Reg 37086C

Target Market(s)

New Home Buyers

Industry/Entity Type

Business

Requirements
Must have
• Sharp detail, Red Black & White colourings.
Should not have
• Any new colours

```html
<!DOCTYPE html>
<html lang="en">
<head>
<meta charset="utf-8">
<title>Dennis Orford Homes – Business Card Front</title>
<link rel="stylesheet" href="https://fonts.googleapis.com/css2?family=Lato:wght@400&display=swap">
<style>
  :root {
    --card-red: #d92826;
    --ink-white: #ffffff;
  }
  html, body {
    margin: 0;
    padding: 0;
    width: 1200px;
    height: 720px;
    overflow: hidden;
    background: var(--card-red);
  }
  .card-front {
    position: relative;
    width: 1200px;
    height: 720px;
    background: var(--card-red);
    color: var(--ink-white);
    font-family: "Lato", "Helvetica Neue", Arial, sans-serif;
    font-weight: 400;
  }
  .brand-name {
    position: absolute;
    left: 0;
    right: 0;
    top: 262px;
    margin: 0;
    text-align: center;
    font-size: 84px;
    line-height: 1;
    letter-spacing: 4px;
    text-transform: uppercase;
    font-weight: 400;
  }
  .brand-name .brand-sub {
    display: block;
    margin-top: 32px;
    font-size: 32px;
    letter-spacing: 12px;
    padding-left: 12px;
  }
  .tagline {
    position: absolute;
    left: 0;
    right: 0;
    top: 632px;
    margin: 0;
    text-align: center;
    font-size: 27px;
    line-height: 1;
    letter-spacing: 0.3px;
    text-transform: uppercase;
  }
  .tagline-rule {
    position: absolute;
    left: 462px;
    top: 682px;
    width: 274px;
    height: 8px;
  }
</style>
</head>
<body>
  <main class="card-front">
    <h1 class="brand-name">Dennis Orford<span class="brand-sub">Homes</span></h1>
    <p class="tagline">Not just a house, it’s your home</p>
    <svg class="tagline-rule" viewBox="0 0 274 8" aria-hidden="true">
      <path d="M0 4 Q137 0 274 4 Q137 8 0 4 Z" fill="var(--ink-white)"/>
    </svg>
  </main>
</body>
</html>
```